Business Card Design

Electrical Contracting buisness
need a buisness card relating to that buisness

Reason: Just need to discuss with partner

Industry/Entity Type

Business

Contact Information for Business Card

Colin Harbage Electrical
0417 562 983
colinharbage7@mailvessel.com
REC 48761

```html
<!DOCTYPE html>
<html lang="en">
<head>
<meta charset="utf-8">
<title>Colin Harbage Electrical – Business Card</title>
<link rel="stylesheet" href="https://fonts.googleapis.com/css2?family=Michroma&display=swap">
<style>
  :root {
    --page-bg: #e9ebee;
    --card-bg: #ffffff;
    --card-shade: #eef0f2;
    --brand-blue: #1f63d6;
    --band-blue-light: #2aa3ee;
    --band-blue-dark: #1a4fcf;
    --accent-grey: #a9adb2;
    --ink: #3a3c40;
    --ink-soft: #55585d;
  }
  * { box-sizing: border-box; margin: 0; padding: 0; }
  html, body {
    width: 1200px; height: 900px; overflow: hidden;
    background: var(--page-bg);
    font-family: "Michroma", sans-serif;
  }
  .card {
    position: absolute; left: 100px; top: 160px;
    width: 1000px; height: 580px;
    border-radius: 42px; overflow: hidden;
    background: radial-gradient(ellipse at 45% 40%, var(--card-bg) 55%, var(--card-shade) 100%);
    box-shadow: 0 14px 40px rgba(0,0,0,0.18);
  }
  .side-bands { position: absolute; inset: 0; }
  .brand {
    position: absolute; left: 200px; top: 90px;
    display: flex; align-items: center; gap: 28px;
  }
  .brand-dot {
    width: 118px; height: 118px; border-radius: 50%;
    background: var(--brand-blue);
  }
  .brand-name {
    color: var(--brand-blue);
    font-size: 36px; line-height: 1.3; letter-spacing: 1px;
    text-transform: uppercase;
  }
  .contact {
    position: absolute; left: 180px; top: 320px; width: 660px;
    display: flex; color: var(--ink);
  }
  .contact-person {
    width: 290px; text-align: right; padding-right: 26px;
    font-size: 16px; line-height: 1.55; letter-spacing: 2px;
  }
  .person-name { font-size: 19px; color: var(--ink); }
  .person-role { color: var(--ink-soft); margin-bottom: 18px; }
  .person-address { color: var(--ink-soft); }
  .contact-divider { width: 1px; height: 165px; background: var(--accent-grey); }
  .contact-lines {
    list-style: none; padding-left: 22px;
    font-size: 16px; line-height: 1.75; letter-spacing: 2px; color: var(--ink);
  }
  .contact-lines li { display: flex; align-items: center; gap: 10px; }
  .contact-lines svg { width: 16px; height: 16px; flex: none; }
</style>
</head>
<body>
  <div class="card">
    <svg class="side-bands" viewBox="0 0 1000 580" width="1000" height="580" aria-hidden="true">
      <defs>
        <linearGradient id="bandLeft" x1="0" y1="0" x2="0" y2="1">
          <stop offset="0" stop-color="var(--band-blue-light)"/>
          <stop offset="1" stop-color="var(--band-blue-dark)"/>
        </linearGradient>
        <linearGradient id="bandRight" x1="0" y1="0" x2="0" y2="1">
          <stop offset="0" stop-color="var(--band-blue-light)"/>
          <stop offset="1" stop-color="var(--band-blue-dark)"/>
        </linearGradient>
      </defs>
      <path d="M0 0 H105 Q40 290 95 580 H0 Z" fill="url(#bandLeft)"/>
      <path d="M120 0 Q55 290 112 580" fill="none" stroke="var(--accent-grey)" stroke-width="9"/>
      <path d="M1000 0 H900 Q965 290 905 580 H1000 Z" fill="url(#bandRight)"/>
      <path d="M882 0 Q948 290 888 580" fill="none" stroke="var(--accent-grey)" stroke-width="9"/>
    </svg>

    <div class="brand">
      <div class="brand-dot"></div>
      <div class="brand-name">Colin Harbage<br>Electrical</div>
    </div>

    <div class="contact">
      <div class="contact-person">
        <p class="person-name">DALE CORRIN</p>
        <p class="person-role">OWNER / C.E.O</p>
        <p class="person-address">SUITE # 14, KELL BLDG,<br>NY 80421</p>
      </div>
      <div class="contact-divider"></div>
      <ul class="contact-lines">
        <li>
          <svg viewBox="0 0 16 16"><circle cx="8" cy="8" r="8" fill="var(--ink)"/><path d="M5 4.5l1.6-.5.9 2-1 .8a5 5 0 0 0 2.7 2.7l.8-1 2 .9-.5 1.6c-3.4.4-6.9-3.1-6.5-6.5z" fill="#fff"/></svg>
          302-555-0147
        </li>
        <li>
          <svg viewBox="0 0 16 16"><circle cx="8" cy="8" r="8" fill="var(--ink)"/><rect x="5.5" y="3.5" width="5" height="9" rx="1" fill="#fff"/><rect x="6.5" y="5" width="3" height="5" fill="var(--ink)"/></svg>
          302-555-0162
        </li>
        <li>
          <svg viewBox="0 0 16 16"><circle cx="8" cy="8" r="8" fill="var(--ink)"/><rect x="4" y="7" width="8" height="5" rx="1" fill="#fff"/><rect x="5.5" y="4" width="5" height="3" fill="#fff"/></svg>
          302-555-0189
        </li>
        <li>
          <svg viewBox="0 0 16 16"><circle cx="8" cy="8" r="8" fill="var(--ink)"/><rect x="4" y="5" width="8" height="6" rx="1" fill="#fff"/><path d="M4.5 5.5L8 8.5l3.5-3" fill="none" stroke="var(--ink)" stroke-width="1"/></svg>
          office@voltharbour.com
        </li>
        <li>
          <svg viewBox="0 0 16 16"><circle cx="8" cy="8" r="8" fill="var(--ink)"/><circle cx="8" cy="8" r="4.5" fill="none" stroke="#fff" stroke-width="1"/><ellipse cx="8" cy="8" rx="2" ry="4.5" fill="none" stroke="#fff" stroke-width="1"/><path d="M3.5 8h9" stroke="#fff" stroke-width="1"/></svg>
          www.voltharbour.com
        </li>
      </ul>
    </div>
  </div>
</body>
</html>
```